Australia-Wide Industry Leader Bookkeeping Business Website Design Required

We need a website designed for our 10 year old bookkeeping business, Barwick & Lund. Barwick & Lund has been servicing the local & interstate communities of Australia, providing first-class BAS & Bookkeeping services with a personal touch unmatched by anyone else in the county.

What began 10 years ago as a small business focusing on family, friends and the local community, it has since grown into a well respected business with 95% of their business based solely on word of mouth and personal referrals from around Australia.

We would like to see designs that incorporate our existing brand/logo. The colours to be used on the website should be colours that work well with our logo. The design should communicate maturity, trust and confidence with a Web 2.0 look and feel.

We have produced mockups of the entire website as well as assets used in the mockups. Please reference the attached files. The mockups are an example of all the design elements that we want on each page. Designers are encouraged to use the mockups as a guideline only and for designers to use their own creativity.
Updates

This message is for new graphic designers who are considering commencing work on this project. Thank you for expressing an interest in our project. We would like to inform you that this project is close to completion as we have a number designs under very serious consideration.

We are currently in a position where we are disinterested providing feedback to improve on new designs submitted. We will provide feedback to improve new designs only if the submitted designs are very close to what we want for our website, and will only require 1 or 2 revision rounds to refine before the project completion date we will not work with designers to refine their newly submitted designs.

We feel that it is important for all designers to know the above information as we feel that your time and effort may be better spent working on another project.

Thank you for your understanding.

A big thank you for all the designs submitted. We are now in the process of selecting a design. Please be patient during this process. Thank you.

Target Market(s)

Busy Business Owners

Industry/Entity Type

Small Business

Requirements
Must have
• We require a rectangular "slide show" type feature to serve as a "teaser" to arouse the emotions of our website visitors. Each slide asks a specific question. The questions are:

- Is your paperwork in a mess?
- Do you need to get organised for the end of financial year?
- Are you sick & tired of endless amounts of paperwork & BASs?
- Do you feel frustrated & annoyed because you know your books need to be done?
- Do you lack the time & patience to get your paperwork done?
- Do you wish you had more time to do the things you enjoy doing?
- Contact Barwick & Lund today and we will transform your chaos into order.

Underneath the slide show will be a button to "Call Barwick & Lund Now - 03 5550 1827".

```html
<!DOCTYPE html>
<html lang="en">
<head>
<meta charset="utf-8">
<title>Barwick &amp; Lund – Bookkeeping &amp; BAS</title>
<link rel="stylesheet" href="https://fonts.googleapis.com/css2?family=Bebas+Neue&family=Oswald:wght@400;500&family=Arimo:wght@400;700&family=Tinos&family=Cinzel+Decorative&display=swap">
<style>
:root{
  --brand:#7a0a12;
  --brand-dark:#5c070d;
  --frame:#3a3a3a;
  --page:#f4f4f4;
  --header:#f8f8f8;
  --footer:#ebebeb;
  --rule:#dcdcdc;
  --text:#555;
  --text-dark:#333;
  --muted:#888;
  --icon:#c9c9c9;
}
*{margin:0;padding:0;box-sizing:border-box}
html,body{width:1041px;height:1200px;overflow:hidden}
body{background:var(--frame);font-family:"Arimo",Arial,sans-serif;color:var(--text);position:relative}
.page{position:absolute;left:34px;top:0;width:989px;height:1200px;background:var(--page);overflow:hidden}
.page > *{position:absolute}
.topbar{left:0;top:0;width:100%;height:6px;background:var(--brand)}
.site-header{left:0;top:6px;width:100%;height:182px;background:var(--header);border-bottom:4px solid #e6e6e6}
.brand{left:201px;top:15px;width:565px;height:110px;border:2px solid #222;background:var(--brand);display:flex;align-items:center;justify-content:center;gap:18px}
.brand-mark{width:22px;height:22px;background:#fff}
.brand-name{font-family:"Tinos",Georgia,serif;font-size:62px;color:#fff;line-height:1}
.main-nav{left:201px;top:126px;display:flex;height:44px}
.main-nav a{font-family:"Oswald",sans-serif;font-size:15px;color:var(--text-dark);text-decoration:none;text-transform:uppercase;line-height:44px;padding:0 16px;margin-right:9px;letter-spacing:.2px}
.main-nav a.active{background:var(--brand);color:#fff}
.hero-title{left:17px;top:234px;width:480px;font-family:"Bebas Neue",sans-serif;font-size:60px;line-height:57px;color:var(--brand);letter-spacing:.5px}
.hero-image{left:540px;top:280px;width:470px;height:140px;display:flex;align-items:center;justify-content:center;font-family:"Cinzel Decorative",serif;font-size:33px;color:#222}
.slide-dots{left:17px;top:459px;display:flex;gap:4px}
.slide-dots span{width:12px;height:12px;background:var(--frame)}
.slide-dots span.current{background:var(--brand)}
.rule{left:17px;width:933px;height:4px;background:var(--rule)}
.rule-accent{left:17px;width:36px;height:4px;background:var(--brand)}
.call-bar{left:17px;top:514px;width:933px;text-align:center;font-family:"Oswald",sans-serif;font-size:20px;color:#4a4a4a;letter-spacing:.3px}
.intro{left:17px;top:578px;width:690px;font-size:13.5px;line-height:20px}
.intro h2{font-family:"Oswald",sans-serif;font-weight:500;font-size:15px;color:var(--brand);margin-bottom:14px;text-transform:uppercase}
.intro p{margin-bottom:15px}
.intro strong{color:var(--brand)}
.intro ul{list-style:none;margin:-6px 0 14px}
.intro li{padding-left:17px;position:relative;line-height:25.5px}
.intro li::before{content:"›";position:absolute;left:0;color:#aaa}
.testimonial{left:739px;top:576px;width:212px;font-family:"Tinos",Georgia,serif;font-size:18.5px;line-height:20px;color:#444}
.testimonial .q{color:#c88a1e}
.map{left:739px;top:693px;width:212px;height:161px;background:linear-gradient(160deg,#fafafa,#e2e2e2)}
.site-footer{left:0;top:997px;width:100%;height:203px;background:var(--footer);border-top:5px solid #dedede}
.social{left:16px;top:1039px;display:flex;gap:11px}
.social span{width:24px;height:24px;border-radius:50%;background:var(--icon)}
.contact{left:494px;top:1011px;font-size:10px;color:#444;line-height:14px}
.contact .email{margin-top:18px}
.contact .email a{color:var(--brand);text-decoration:none}
.footer-rule{left:17px;top:1113px;width:933px;height:1px;background:#d0d0d0}
.legal{left:17px;top:1120px;font-size:10px;color:var(--muted);line-height:17px}
.legal nav a,.legal-links a{color:var(--muted);text-decoration:none;text-transform:uppercase;margin-right:11px}
.legal-links{right:36px;top:1128px;font-size:10px}
.legal-links a{margin:0 0 0 9px}
.to-top{left:460px;top:1136px;width:44px;height:44px;border-radius:50%;background:#dcdcdc;font-size:9px;color:#999;display:flex;align-items:center;justify-content:center}
</style>
</head>
<body>
<div class="page">
  <div class="topbar"></div>
  <header class="site-header"></header>
  <div class="brand"><span class="brand-mark"></span><span class="brand-name">Barwick &amp; Lund</span></div>
  <nav class="main-nav">
    <a class="active" href="#">Home</a><a href="#">Company</a><a href="#">Services</a><a href="#">Testimonials</a><a href="#">ATO Dates</a><a href="#">Contact</a>
  </nav>

  <h1 class="hero-title">Are you sick &amp; tired of endless amounts of paperwork &amp; BASs?</h1>
  <div class="hero-image">354 * 250 Image</div>
  <div class="slide-dots"><span></span><span></span><span class="current"></span><span></span><span></span><span></span><span></span></div>

  <div class="rule" style="top:490px"></div>
  <div class="call-bar">"CALL BARWICK &amp; LUND NOW - 03 5550 1827"</div>
  <div class="rule" style="top:553px"></div>
  <div class="rule-accent" style="top:553px"></div>

  <section class="intro">
    <h2>Welcome to Barwick &amp; Lund</h2>
    <p>Barwick &amp; Lund provide industry-focused, <strong>Bookkeeping</strong>, <strong>Payroll</strong> and <strong>Office Administration</strong> services that are designed to increase and improve your performance and processes for public and private clients.</p>
    <p>We are a unique organization, with the skills and ability to improve the function of your business, as we work with a team of elite accountants and wealth creation professionals who coach us in:</p>
    <p>Advanced up to date tax strategies</p>
    <ul>
      <li>Tax structures (and the best tax savings)</li>
      <li>Asset protection</li>
      <li>Superannuation &amp; Self Managed Super Funds</li>
      <li>Property and personal Investing</li>
      <li>Stock &amp; Options trading</li>
      <li>Secure Offshore Investing</li>
    </ul>
    <p>With over 30 years experience, we guarantee the quality of our work.</p>
  </section>

  <blockquote class="testimonial"><span class="q">"</span> The detail and accuracy is exceptionable, leaving me with no doubt that my documentation is in safe hands — Ledgerline <span class="q">"</span></blockquote>
  <div class="map" role="img" aria-label="Map of Australia marking client locations"></div>

  <footer class="site-footer"></footer>
  <div class="social"><span></span><span></span><span></span><span></span><span></span><span></span></div>
  <div class="contact">
    <div>Address: Barwick &amp; Lund P.O. Box 417 Kernvale&nbsp; 3188&nbsp; VIC T: (03) 9550 4412 F: (03) 9550 4413</div>
    <div class="email">E-mail: <a href="#">hello@barwicklund.example</a></div>
  </div>
  <div class="footer-rule"></div>
  <div class="legal">
    <div>Copyright © 2012 Barwick &amp; Lund. All rights reserved</div>
    <nav><a href="#">Home</a><a href="#">About</a><a href="#">Services</a><a href="#">Testimonials</a><a href="#">ATO Dates</a><a href="#">Contact</a></nav>
  </div>
  <div class="legal-links"><a href="#">FAQ</a><a href="#">Privacy Statement</a><a href="#">Terms and Conditions</a></div>
  <div class="to-top">TOP</div>
</div>
</body>
</html>
```